Tovrel Business Card

We are a modern retail clothing store. Established in 1994. I need a presentable card that will amaze vendors when given to them.

Front: Logo in middle
Info Side:

Name: Omar Latif
Cell: 630-555-0148
Work: 630-555-0192 EXT. 417
Email: Omar@tovrel.example
Website: www.Tovrel.example

Industry/Entity Type

Business

```html
<!DOCTYPE html>
<html lang="en">
<head>
<meta charset="UTF-8">
<title>Tovrel Business Card</title>
<link href="https://fonts.googleapis.com/css2?family=Open+Sans:wght@400;600;700;800&display=swap" rel="stylesheet">
<style>
  :root {
    --backdrop: #2a2a2a;
    --card: #ffffff;
    --ink: #0b0b0b;
    --paper-text: #ffffff;
  }
  * { margin: 0; padding: 0; box-sizing: border-box; }
  html, body {
    width: 1200px; height: 900px; overflow: hidden;
    background: var(--backdrop);
    font-family: "Open Sans", Arial, sans-serif;
  }
  .stage {
    width: 1200px; height: 900px;
    display: flex; flex-direction: column; align-items: center; justify-content: center;
    gap: 56px;
  }
  .card {
    position: relative;
    width: 620px; height: 354px;
    background: var(--card);
    border-radius: 22px;
    overflow: hidden;
    box-shadow: 0 10px 24px rgba(0,0,0,0.45);
  }
  /* Front */
  .front .wordmark {
    position: absolute; left: 0; right: 0; top: 108px;
    text-align: center;
    font-size: 92px; font-weight: 800; letter-spacing: 4px;
    color: var(--ink); line-height: 1;
  }
  .front .site {
    position: absolute; left: 0; right: 0; top: 262px;
    text-align: center; font-size: 15px; color: var(--ink);
  }
  .front .site b { font-weight: 700; }
  /* Back */
  .rule { position: absolute; left: 0; right: 0; background: var(--ink); }
  .rule.top { top: 92px; height: 6px; }
  .rule.bottom { top: 270px; height: 6px; }
  .band {
    position: absolute; left: 0; right: 0; top: 110px; height: 148px;
    background: var(--ink); color: var(--paper-text);
    display: flex; align-items: center;
  }
  .brand { width: 320px; padding-left: 48px; }
  .brand .wordmark {
    font-size: 62px; font-weight: 800; letter-spacing: 3px; line-height: 1;
  }
  .brand .since { font-size: 18px; font-weight: 600; margin-top: 4px; letter-spacing: 0.5px; }
  .divider { width: 1px; height: 104px; background: rgba(255,255,255,0.55); }
  .contact { padding-left: 28px; }
  .contact .name { font-size: 21px; font-weight: 700; letter-spacing: 0.5px; margin-bottom: 8px; }
  .contact ul { list-style: none; }
  .contact li { display: flex; align-items: center; gap: 9px; font-size: 13.5px; line-height: 19px; }
  .contact svg { width: 11px; height: 11px; flex: none; }
</style>
</head>
<body>
<main class="stage">
  <section class="card front">
    <div class="wordmark">TOVREL</div>
    <div class="site">www.<b>Tovrel</b>.example</div>
  </section>

  <section class="card back">
    <div class="rule top"></div>
    <div class="band">
      <div class="brand">
        <div class="wordmark">TOVREL</div>
        <div class="since">Established in 1994</div>
      </div>
      <div class="divider"></div>
      <div class="contact">
        <div class="name">OMAR LATIF</div>
        <ul>
          <li>
            <svg viewBox="0 0 12 12"><rect x="3" y="0.5" width="6" height="11" rx="1" fill="none" stroke="#fff" stroke-width="1.3"/><circle cx="6" cy="9.5" r="0.8" fill="#fff"/></svg>
            630-555-0148
          </li>
          <li>
            <svg viewBox="0 0 12 12"><path d="M2.5 1 L4.5 1 L5.3 3.6 L4 4.6 Q5 7 7.4 8 L8.4 6.7 L11 7.5 L11 9.5 Q11 11 9.5 11 Q1 10 1 2.5 Q1 1 2.5 1 Z" fill="#fff"/></svg>
            630-555-0192 EXT. 417
          </li>
          <li>
            <svg viewBox="0 0 12 12"><rect x="0.7" y="2.2" width="10.6" height="7.6" fill="none" stroke="#fff" stroke-width="1.2"/><path d="M0.7 2.4 L6 6.6 L11.3 2.4" fill="none" stroke="#fff" stroke-width="1.2"/></svg>
            Omar@tovrel.example
          </li>
          <li>
            <svg viewBox="0 0 12 12"><circle cx="6" cy="6" r="5.2" fill="none" stroke="#fff" stroke-width="1.1"/><ellipse cx="6" cy="6" rx="2.2" ry="5.2" fill="none" stroke="#fff" stroke-width="1"/><path d="M0.8 6 H11.2" stroke="#fff" stroke-width="1"/></svg>
            www.Tovrel.example
          </li>
        </ul>
      </div>
    </div>
    <div class="rule bottom"></div>
  </section>
</main>
</body>
</html>
```